Small business updating business cards

We have already updated our logo via Pixel Forum and downloaded it (hopefully) for you to use. Now an updated set of business cards for Neil Pollard and Stuart Pollard are also needed... we are also hoping that a copy of our outdated business card designs have uploaded successfully as Microsoft Publisher files. Our Strength Through Unity motto has died a slow death so we are hoping to remove it (and other superfluous lingo if the graphic covers the idea) and instead opt for a fancy graphic (?) on the second side of the card that really reflects our desire to obtain product / haulage from Road Transport / Yard Operators and convert legs of their haulage to rail freight where profitable (bulk haulage / containterised etc). Can you help us look larger, bolder and more robust than we really are (two man show)?
Target Market(s)
Transport Industry
Industry/Entity Type
Business
Contact Information for Business Card
Card details for both N Pollard and S Pollard have been uploaded on the publisher files
Colors
Designer to choose colors to be used in the design.
Requirements
Must have
- Similar theme both sides of card
Should not have
- Black on one side white on the other

```html
<!DOCTYPE html>
<html lang="en">
<head>
<meta charset="utf-8">
<title>Norvale Freight – Business Cards</title>
<link rel="stylesheet" href="https://fonts.googleapis.com/css2?family=Roboto:wght@400;500;700&family=Roboto+Slab:wght@400;700&display=swap">
<style>
  :root {
    --stage: #4b4b4b;
    --paper: #ffffff;
    --ink: #111111;
    --teal: #2b8a9d;
    --gold: #a69a36;
    --gold-line: #c59b2f;
    --white: #ffffff;
  }
  * { margin: 0; padding: 0; box-sizing: border-box; }
  html, body { width: 900px; height: 1200px; overflow: hidden; }
  body {
    position: relative;
    background: var(--stage);
    font-family: "Roboto", Arial, sans-serif;
    color: var(--ink);
  }
  .card {
    position: absolute;
    left: 80px;
    width: 734px;
    height: 430px;
    overflow: hidden;
    box-shadow: 0 6px 12px rgba(0,0,0,.45);
  }
  .card--front { top: 147px; background: var(--paper); }
  .card--back {
    top: 629px;
    background: linear-gradient(180deg, var(--teal) 0%, #2e8a9a 20%, #8a9760 65%, var(--gold) 100%);
  }

  .ring { position: absolute; left: 0; top: 0; }

  .name-band {
    position: absolute;
    left: 0; top: 160px;
    width: 734px; height: 57px;
    background: linear-gradient(90deg, var(--gold) 0%, #7e9468 35%, #3c8c95 62%, var(--teal) 100%);
  }
  .bracket {
    position: absolute;
    top: 140px;
    width: 20px; height: 95px;
    border: 6px solid var(--ink);
  }
  .bracket--open { left: 175px; border-right: none; }
  .bracket--close { left: 657px; border-left: none; border-color: var(--gold-line); }

  .tagline {
    position: absolute;
    left: -131px; top: 185px;
    width: 370px; height: 60px;
    transform: rotate(-90deg);
    font-family: "Roboto Slab", Georgia, serif;
    font-weight: 700;
    font-size: 16.5px;
    line-height: 28px;
    letter-spacing: .2px;
    text-align: left;
    white-space: nowrap;
  }

  .brand {
    position: absolute;
    font-family: "Roboto", Arial, sans-serif;
    font-weight: 700;
    white-space: nowrap;
  }
  .brand--front {
    left: 250px; top: 52px; width: 350px;
    text-align: center;
    font-size: 50px;
    color: var(--teal);
  }
  .brand--back {
    left: 0; top: 185px; width: 734px;
    text-align: center;
    font-size: 56px;
    color: var(--white);
  }

  .holder-name {
    position: absolute;
    left: 195px; top: 168px; width: 462px;
    text-align: center;
    font-family: "Roboto Slab", Georgia, serif;
    font-size: 31px;
    color: var(--white);
    letter-spacing: .5px;
  }
  .holder-role {
    position: absolute;
    left: 195px; top: 225px; width: 462px;
    text-align: center;
    font-family: "Roboto Slab", Georgia, serif;
    font-size: 19px;
  }

  .address {
    position: absolute;
    left: 122px; top: 271px; width: 260px;
    text-align: center;
    font-size: 18px;
    line-height: 23px;
  }
  .address__heading { font-weight: 500; margin-top: 7px; font-size: 17px; }

  .contact {
    position: absolute;
    left: 385px; top: 311px; width: 340px;
    text-align: center;
    font-size: 16.5px;
    line-height: 24px;
  }

  .service-line {
    position: absolute;
    left: 0; top: 354px; width: 734px;
    text-align: center;
    font-family: "Roboto Slab", Georgia, serif;
    font-size: 16.5px;
    line-height: 23px;
    color: var(--white);
  }
</style>
</head>
<body>

<section class="card card--front" aria-label="Business card front">
  <svg class="ring" width="734" height="430" aria-hidden="true">
    <circle cx="205" cy="213" r="183" fill="none" stroke="var(--gold-line)" stroke-width="2.5"/>
  </svg>
  <div class="name-band"></div>
  <div class="bracket bracket--open"></div>
  <div class="bracket bracket--close"></div>

  <p class="tagline">STRATEGIC ALLIANCE PARTNERS<br>PROVIDING LOGISTICAL FREIGHT<br>SOLUTIONS</p>

  <p class="brand brand--front">Norvale Freight</p>

  <h1 class="holder-name">NEIL POLLARD</h1>
  <p class="holder-role">DIRECTOR</p>

  <div class="address">
    <p>14 Tarrin Street</p>
    <p>Coral Flats NSW 2290</p>
    <p class="address__heading">Alternate emails</p>
    <p>norvalefreight@mailbox.com</p>
    <p>norvalefreight@postnet.com</p>
  </div>

  <div class="contact">
    <p>Mobile: 0400 555 018</p>
    <p>Email: pollardn@norvalefreight.com.au</p>
  </div>
</section>

<section class="card card--back" aria-label="Business card back">
  <p class="brand brand--back">Norvale Freight</p>
  <p class="service-line">Haulage from Road Transport / Yard Operators and convert legs of their<br>haulage to rail freight where profitable (bulk haulage / containterised etc)</p>
</section>

</body>
</html>
```